Harrowfield Nature Alliance needs a poster for fish fry

We need a flyer made for a fish fry. Things we need on it;

Date: Sunday, February 12th
Location: Brenmoor Sportsdome Auditorium
Time: 5-6:30 pm
Cost: $15 for adults, $10 for 12 & under, free for preschool

Requirements
Must have
• Must have our logo on it.

```html
<!DOCTYPE html>
<html lang="en">
<head>
<meta charset="utf-8">
<title>Fish Fry Poster – Harrowfield Nature Alliance</title>
<link rel="stylesheet" href="https://fonts.googleapis.com/css2?family=Anton&family=Montserrat:wght@800&display=swap">
<style>
  :root {
    --page: #ece9ec;
    --sky-top: #ddd3de;
    --sky-mid: #a9a7b3;
    --hills: #51636a;
    --forest: #22393a;
    --grass: #b4935a;
    --teal: #2e6b74;
    --ink: #111111;
    --white: #ffffff;
    --gold: #e2c48a;
    --box-ink: #1f2f31;
  }
  * { margin: 0; padding: 0; box-sizing: border-box; }
  html, body { width: 1200px; height: 800px; overflow: hidden; background: var(--page); }
  .canvas { position: relative; width: 1200px; height: 800px; }
  .poster {
    position: absolute; left: 330px; top: 20px; width: 540px; height: 760px;
    overflow: hidden; box-shadow: 0 6px 24px rgba(0,0,0,.18);
  }
  .poster__scene {
    position: absolute; inset: 0;
    background:
      radial-gradient(ellipse 70% 40% at 95% 100%, var(--grass) 0%, rgba(180,147,90,.5) 45%, transparent 75%),
      linear-gradient(180deg, var(--sky-top) 0%, #d6cdd7 32%, var(--sky-mid) 50%, var(--hills) 64%, var(--forest) 82%, #1c302f 100%);
  }
  .poster__content { position: relative; text-align: center; padding-top: 58px; }
  .title {
    font-family: "Anton", sans-serif; font-size: 108px; line-height: 1;
    color: var(--teal); letter-spacing: 1px;
  }
  .event-line {
    font-family: "Anton", sans-serif; line-height: 1.12; letter-spacing: 1px;
  }
  .event-line--day { font-size: 40px; color: var(--ink); margin-top: 22px; }
  .event-line--date { font-size: 40px; color: var(--teal); }
  .event-line--time { font-size: 40px; color: var(--ink); }
  .event-line--venue { font-size: 36px; color: var(--teal); margin-top: 10px; }
  .cost {
    display: flex; margin: 34px auto 0; width: 410px; height: 124px;
    border: 2px solid var(--white); border-radius: 14px; overflow: hidden;
  }
  .cost__label {
    width: 62px; background: var(--white); display: flex; align-items: center; justify-content: center;
  }
  .cost__label span {
    display: block; transform: rotate(-90deg);
    font-family: "Anton", sans-serif; font-size: 34px; color: var(--box-ink); letter-spacing: 1px;
  }
  .cost__list {
    list-style: none; flex: 1; display: flex; flex-direction: column; justify-content: center;
    padding-left: 22px; text-align: left;
    font-family: "Montserrat", sans-serif; font-weight: 800; font-size: 24px; line-height: 1.3;
    color: var(--white);
  }
  .cost__price { color: var(--gold); }
  .marks {
    display: flex; justify-content: center; align-items: center; gap: 60px; margin-top: 46px;
  }
  .marks__stamp { width: 120px; height: 120px; }
  .org { display: flex; align-items: center; gap: 12px; }
  .org__dot { width: 18px; height: 18px; border-radius: 50%; background: var(--white); }
  .org__name {
    font-family: "Montserrat", sans-serif; font-weight: 800; font-size: 20px;
    line-height: 1.15; color: var(--white); text-align: left; text-transform: uppercase;
  }
</style>
</head>
<body>
<div class="canvas">
  <article class="poster">
    <div class="poster__scene" role="img" aria-label="Misty mountain ridges fading into a forested valley with golden grass on a hillside"></div>
    <div class="poster__content">
      <h1 class="title">FISH FRY</h1>
      <p class="event-line event-line--day">SUNDAY,</p>
      <p class="event-line event-line--date">FEBRUARY 12TH, 2023</p>
      <p class="event-line event-line--time">5-6:30 PM</p>
      <p class="event-line event-line--venue">BRENMOOR SPORTSDOME<br>AUDITORIUM</p>
      <div class="cost">
        <div class="cost__label"><span>COST</span></div>
        <ul class="cost__list">
          <li><span class="cost__price">$15</span> FOR ADULTS</li>
          <li><span class="cost__price">$10</span> FOR 12 &amp; UNDER</li>
          <li><span class="cost__price">FREE</span> FOR PRESCHOOL</li>
        </ul>
      </div>
      <div class="marks">
        <svg class="marks__stamp" viewBox="0 0 120 120" aria-hidden="true">
          <circle cx="60" cy="60" r="56" fill="none" stroke="#ffffff" stroke-width="5"/>
        </svg>
        <div class="org">
          <span class="org__dot"></span>
          <p class="org__name">Harrowfield<br>Nature Alliance</p>
        </div>
      </div>
    </div>
  </article>
</div>
</body>
</html>
```